Business Card Design

timberline cabinetry in Colorado. We recently changed our logo the use the colors grey and blue. Our company motto is "where ideas come to life" Wanting a business card to pop and stand out. I attached our new logo and colors scheme

Industry/Entity Type

Business

```html
<!DOCTYPE html>
<html lang="en">
<head>
<meta charset="UTF-8">
<title>Timberline Cabinetry Company – Business Card</title>
<link href="https://fonts.googleapis.com/css2?family=Oswald:wght@700&family=Satisfy&display=swap" rel="stylesheet">
<style>
  :root {
    --wood-light: #d9b78f;
    --wood-mid: #c49a6c;
    --wood-dark: #a97d52;
    --ink: #ffffff;
    --frame: #ffffff;
    --brand-blue: #2f6fa8;
    --brand-grey: #6f7479;
    --photo-warm-a: #e9dccb;
    --photo-warm-b: #a88a68;
    --photo-cool-a: #dcd6cf;
    --photo-cool-b: #6d6a68;
  }
  html, body {
    margin: 0;
    padding: 0;
    overflow: hidden;
    background: #ffffff;
  }
  .card {
    position: relative;
    width: 1200px;
    height: 703px;
    overflow: hidden;
  }
  .wood-backdrop {
    position: absolute;
    inset: 0;
    background: linear-gradient(120deg, var(--wood-light) 0%, var(--wood-mid) 55%, var(--wood-dark) 100%);
  }
  .brand {
    position: absolute;
    left: 72px;
    top: 66px;
    display: flex;
    align-items: flex-start;
    gap: 14px;
  }
  .brand-name {
    margin: 0;
    font-family: "Oswald", "Arial Narrow", sans-serif;
    font-weight: 700;
    font-size: 60px;
    line-height: 60px;
    letter-spacing: -1px;
    text-transform: uppercase;
    color: var(--ink);
  }
  .brand-mark {
    width: 34px;
    height: 34px;
    margin-top: 12px;
    background: var(--brand-blue);
    box-shadow: 0 0 0 4px var(--brand-grey);
  }
  .tagline {
    position: absolute;
    left: 72px;
    top: 272px;
    margin: 0;
    font-family: "Satisfy", cursive;
    font-size: 48px;
    line-height: 56px;
    white-space: nowrap;
    color: var(--ink);
    text-shadow: 0 1px 3px rgba(80, 50, 20, 0.35);
  }
  .contact {
    position: absolute;
    left: 72px;
    top: 380px;
    width: 560px;
    margin: 0;
    padding: 0;
    list-style: none;
    font-family: "Satisfy", cursive;
    font-size: 35px;
    line-height: 53px;
    white-space: nowrap;
    color: var(--ink);
    text-shadow: 0 1px 3px rgba(80, 50, 20, 0.35);
  }
  .showcase-photo {
    position: absolute;
    margin: 0;
    background: var(--frame);
    padding: 9px;
    box-shadow: 2px 4px 10px rgba(60, 35, 10, 0.45);
  }
  .showcase-photo .fill {
    width: 100%;
    height: 100%;
  }
  .showcase-photo--light {
    left: 748px;
    top: 70px;
    width: 346px;
    height: 222px;
    transform: rotate(3deg);
  }
  .showcase-photo--light .fill {
    background: linear-gradient(180deg, var(--photo-warm-a) 0%, #f7f4ef 45%, var(--photo-warm-b) 100%);
  }
  .showcase-photo--grey {
    left: 690px;
    top: 362px;
    width: 382px;
    height: 214px;
    transform: rotate(-4deg);
  }
  .showcase-photo--grey .fill {
    background: linear-gradient(90deg, var(--photo-cool-a) 0%, var(--photo-cool-b) 55%, var(--photo-cool-a) 100%);
  }
</style>
</head>
<body>
  <main class="card">
    <div class="wood-backdrop" role="img" aria-label="Light pine wood planks laid diagonally"></div>

    <div class="brand">
      <h1 class="brand-name">Timberline<br>Cabinetry<br>Company</h1>
      <span class="brand-mark" aria-hidden="true"></span>
    </div>
    <p class="tagline">where ideas come to life</p>

    <ul class="contact">
      <li>name: timberline cabinetry</li>
      <li>address: 000 aspen way, denver</li>
      <li>phone: 000-000-0000</li>
      <li>email: hello@timberlinecab.com</li>
      <li>website: timberlinecab.com</li>
    </ul>

    <figure class="showcase-photo showcase-photo--light">
      <div class="fill" role="img" aria-label="Photo of a white and oak fitted kitchen with wall cabinets and open shelves"></div>
    </figure>
    <figure class="showcase-photo showcase-photo--grey">
      <div class="fill" role="img" aria-label="Photo of a modern grey kitchen with tall units and an oven"></div>
    </figure>
  </main>
</body>
</html>
```